Trindle Salve by Petal Wrens: All Natural Lip Balm Co. Looking for New Label

Greetings, our company is called Petal Wrens and we are a start-up founded in early 2014. We make 100% All-Natural lip balm, called Trindle Salve, in a variety of flavors and we are looking for a new label that incorporates part of our logo and highlights our product name and our lip balms flavor (see attached files). Our website is: trindlesalve.example, and we are on Twitter: @PetalWrensSalves, and Facebook: /PetalWrensSalves. Our lip balms are made with beeswax, sweet almond oil, shea butter, coconut oil and other all natural oils and flavors.

The design should be clean, and communicate comfort, its "all-natural-ness", reliability, and fun. The colors we would like to have incorporated are burgundy, a deep, but not dark orange (see files, website, logo, graphics), some green and maybe gold/yellow. Given that the lip balm tubes are small (standard tubes), we would like to assure that the lip balm name, the flavor, and part of the logo- (perhaps the bee), are clearly visible and easily read. I am open to a variety of fonts, as long as they convey what I have stated above.

We want to use the label graphics and our logo for not only labeling our product, but also for use on our website, on banners, signs, retail boxes, letterhead, tee shirts, etc. If we like the design we are open to working with you again as our company is growing and we will be expanding our product line within the year to include hand and body balms, as well as other similar items and we will eventually have a few different product lines marketed at various age groups as well. Our lip balm is currently marketed to 14 to 40+ demographic, with the average age being roughly in the 15 to 24 range and our lip balm has been purchased by more women than men, though we market to both.

As far as software goes, I would like it to be in a format that is most popular- my old logo and graphics were made in Adobe Creative Suite 5.0, Adobe InDesign, and Adobe Illustrator, so the label should be made using this software (or a higher version). If I can have the label in a JPEG format also so I personally can add it to my website and social media that would be great.

I have a label redesign doc in an indd format but it was too large to upload. I believe this was the entire layout of our last label. If you need this, or anything else, please let me know as well as how I can send it to you.

We have applied to the popular TV show Otter Court and recently received a call back with interest from the producers; we are so excited and hope you are as well!

Thank you!
Gregor Tallowby
Owner
Petal Wrens Salves LLC
Gregor@PetalWrensSalves.example

The Label dimensions are: 2.25 inches wide ---> by 2 inches long. Currently, there is a .75 inch area that is part of the label and is perforated, used as a safety seal. I may be changing the labels to a slightly different kind but the dimensions will be the same. The tubes we use are standard lip balm tubes with a net weight of .15 ounces ( the total length of the tube from the bottom turning piece to the top of the cap is just over 2.5 inches (this is NOT how large the label must be).We are discontinuing the 1 Hive, 2 Hive concepts ( for different consistencies of the balm) so that part of the label does not need to be included.Feel free to enhance and/or modify the logo to fit the design of the label.Thank you! Added Thursday, February 12, 2015

Requirements
Must have
• Label Dimensions:
• Length: 2.125" Height: 2.125"
• Top Margin: 1.025" Bottom Margin: 1.025"
• Left Margin: 0.9125" Right Margin: 0.9125"
• Horizontal Spacing: 0.15" Vertical Spacing: 0.15"
• Horizontal Pitch: 2.275" Vertical Pitch: 2.275"

```html
<!DOCTYPE html>
<html lang="en">
<head>
<meta charset="utf-8">
<title>Trindle Salve – Beeswax Lip Balm Label</title>
<link href="https://fonts.googleapis.com/css2?family=Montserrat:wght@600;700&family=Open+Sans:wght@400;600&display=swap" rel="stylesheet">
<style>
  :root {
    --page: #ececec;
    --label: #ffffff;
    --orange: #f39c1f;
    --orange-soft: #fbe3c0;
    --burgundy: #8b2536;
    --cocoa: #6b4423;
    --white: #ffffff;
  }
  * { margin: 0; padding: 0; box-sizing: border-box; }
  html, body { width: 1200px; height: 857px; overflow: hidden; background: var(--page); }
  .canvas { position: relative; width: 1200px; height: 857px; }
  .label {
    position: absolute; left: 222px; top: 52px; width: 756px; height: 756px;
    background: var(--label); font-family: "Montserrat", Arial, sans-serif; color: var(--orange);
  }
  .honeycomb-field {
    position: absolute; left: 0; top: 0; width: 651px; height: 756px;
    background:
      radial-gradient(ellipse at 30% 55%, rgba(251,227,192,0.55), rgba(255,255,255,0) 70%),
      linear-gradient(180deg, rgba(251,227,192,0.25), rgba(255,255,255,0.1));
  }
  .seal-band {
    position: absolute; left: 651px; top: 0; width: 105px; height: 756px; background: var(--orange);
  }
  .seal-text {
    position: absolute; left: 52px; width: 340px; transform-origin: 0 0; transform: rotate(90deg) translate(0, -50%);
    color: var(--white); font-weight: 700; font-size: 16px; white-space: nowrap; text-align: center;
  }
  .seal-text.first { top: 22px; }
  .seal-text.second { top: 402px; }
  .mark { position: absolute; border-radius: 50%; background: var(--orange); }
  .product-name { position: absolute; font-weight: 700; color: var(--orange); white-space: nowrap; letter-spacing: -1px; }
  .product-name.hero { left: 30px; top: 240px; font-size: 48px; }
  .product-name.small { left: 36px; top: 610px; font-size: 34px; }
  .net-weight { position: absolute; left: 118px; top: 350px; font-size: 15px; font-weight: 700; }
  .maker { position: absolute; color: var(--burgundy); font-weight: 600; white-space: nowrap; }
  .maker.top { left: 412px; top: 166px; font-size: 30px; }
  .maker.bottom { left: 34px; top: 518px; font-size: 28px; }
  .maker small { font-size: 10px; vertical-align: top; margin-left: 3px; }
  .product-type {
    position: absolute; text-align: center; font-weight: 700; white-space: nowrap;
    border-top: 2px solid var(--orange); border-bottom: 2px solid var(--orange);
  }
  .product-type.top { left: 396px; top: 235px; width: 230px; font-size: 19px; padding: 3px 0; }
  .product-type.bottom { left: 36px; top: 687px; width: 200px; font-size: 16px; padding: 3px 0; }
  .flavor-tab {
    position: absolute; left: 378px; top: 283px; width: 273px; height: 50px; background: var(--cocoa);
    color: var(--white); font-size: 20px; font-weight: 700; line-height: 50px; padding-left: 17px;
  }
  .ingredients { position: absolute; left: 231px; top: 436px; width: 398px; font-family: "Open Sans", Arial, sans-serif; text-align: justify; }
  .ingredients p { font-size: 12.5px; line-height: 1.35; }
  .ingredients p + p { font-size: 10px; margin-top: 8px; }
  .ingredients strong { font-weight: 600; }
  .contacts { position: absolute; left: 294px; top: 596px; font-weight: 600; font-size: 19px; line-height: 31px; }
  .contacts .social::before {
    content: ""; display: inline-block; width: 22px; height: 22px; background: var(--orange);
    vertical-align: -4px; margin-right: 22px;
  }
  .contacts .web { margin-top: 3px; }
</style>
</head>
<body>
<div class="canvas">
  <div class="label">
    <div class="honeycomb-field" role="img" aria-label="Faint white-and-cream honeycomb pattern"></div>

    <div class="mark" style="left:128px; top:60px; width:110px; height:110px;"></div>
    <div class="product-name hero">TrindleSalve</div>
    <div class="net-weight">Net Weight: 15oz</div>

    <div class="mark" style="left:470px; top:60px; width:100px; height:100px;"></div>
    <div class="maker top">PetalWrens<small>LLC</small></div>
    <div class="product-type top">BEESWAX LIP BALM</div>
    <div class="flavor-tab">Brown Sugar Cookie</div>

    <div class="mark" style="left:88px; top:412px; width:100px; height:100px;"></div>
    <div class="maker bottom">PetalWrens<small>LLC</small></div>

    <div class="ingredients">
      <p><strong>INGREDIENTS:</strong> Lorem ipsum dolor sit amet, consectetur adipisicing elit, sed do eiusmod tempor incididunt ut labore et dolore magna aliqua. Ut enim ad minim veniam, quis nostrud exercitation.</p>
      <p>Lorem ipsum dolor sit amet, consectetur adipisicing elit, sed do eiusmod tempor incididunt ut labore et dolore magna aliqua. Ut enim ad minim veniam, quis nostrud exercitation.</p>
    </div>

    <div class="product-name small">TrindleSalve</div>
    <div class="product-type bottom">BEESWAX LIP BALM</div>

    <div class="contacts">
      <div class="social">PetalWrensSalves</div>
      <div class="social">PetalWrensSalves</div>
      <div class="web">www.petalwrenssalves.example</div>
      <div>PO Box 17 Harrowmere, VT 05999</div>
    </div>

    <div class="seal-band">
      <div class="seal-text first">100% All-Natural Beeswax Lip balm</div>
      <div class="seal-text second">100% All-Natural Beeswax Lip balm</div>
    </div>
  </div>
</div>
</body>
</html>
```